Business card

We are looking for a creative person to deigns our company business card.

Target Market(s)

College age student

Industry/Entity Type

Accommodation

Contact Information for Business Card

We want a fun, clean and sophisticated design. It should look good, but more importantly the information should be legible.

Font styles to use
Serif
Sans Serif
Other font styles liked:
• Open Sans ,

Colors
33a6d7

Requirements
Must have
• Must have a young and memorable message. Be legible.
• Our logo on the back on a solid blue , please find color and logo attached
• LodgeBridgely.net on the back.
Nice to have
• I would like to have couple of different fonts on the LodgeBridgely.net on the back of the cards with a solid blue.

```html
<!DOCTYPE html>
<html lang="en">
<head>
<meta charset="UTF-8">
<title>LodgeBridgely business card</title>
<link href="https://fonts.googleapis.com/css2?family=Arimo:wght@400;700&display=swap" rel="stylesheet">
<style>
  :root {
    --backdrop: #151719;
    --card: #1c2327;
    --card-edge: #232b30;
    --blue: #3a9ad9;
    --blue-deep: #1f6aa6;
    --rule: #2f8fcf;
  }
  * { margin: 0; padding: 0; box-sizing: border-box; }
  html, body { width: 1200px; height: 800px; overflow: hidden; }
  body {
    background: var(--backdrop);
    font-family: "Arimo", Arial, sans-serif;
    position: relative;
  }
  .card {
    position: absolute;
    top: 250px;
    width: 520px;
    height: 297px;
    background: var(--card);
    border: 1px solid var(--card-edge);
    box-shadow: 0 18px 40px rgba(0,0,0,.55);
    color: var(--blue);
  }
  .card--front { left: 50px; }
  .card--back { left: 630px; }

  .brand {
    display: flex;
    align-items: center;
    gap: 10px;
    font-weight: 700;
    color: var(--blue);
    letter-spacing: -0.5px;
  }
  .brand__mark {
    background: var(--blue);
    flex: none;
  }
  .card--front .brand {
    position: absolute;
    left: 50%;
    top: 50%;
    transform: translate(-50%, -50%);
    font-size: 40px;
  }
  .card--front .brand__mark { width: 30px; height: 30px; }

  .card--back .brand {
    position: absolute;
    right: 34px;
    top: 40px;
    font-size: 26px;
  }
  .card--back .brand__mark { width: 20px; height: 20px; }

  .divider {
    position: absolute;
    left: 34px;
    right: 34px;
    top: 150px;
    height: 1px;
    background: var(--rule);
  }
  .holder {
    position: absolute;
    left: 34px;
    top: 118px;
  }
  .holder__name { font-size: 19px; font-weight: 400; letter-spacing: 0.5px; }
  .holder__role { font-size: 14px; margin-top: 12px; }

  .contacts {
    position: absolute;
    left: 34px;
    bottom: 34px;
    list-style: none;
    font-size: 13px;
  }
  .contacts li {
    display: flex;
    align-items: center;
    gap: 8px;
    margin-top: 7px;
  }
  .contacts svg { width: 15px; height: 15px; flex: none; }

  .address {
    position: absolute;
    right: 34px;
    top: 172px;
    text-align: right;
    font-size: 13px;
    line-height: 1.45;
  }
</style>
</head>
<body>

  <section class="card card--front" aria-label="Card front">
    <div class="brand"><span class="brand__mark"></span>LodgeBridgely</div>
  </section>

  <section class="card card--back" aria-label="Card back">
    <div class="brand"><span class="brand__mark"></span>LodgeBridgely</div>

    <div class="holder">
      <p class="holder__name">MARO KELLEN</p>
      <p class="holder__role">CEO</p>
    </div>
    <div class="divider"></div>

    <p class="address">PO BOX 456 Harbour Lane<br>3rd street Kestrel Bay</p>

    <ul class="contacts">
      <li>
        <svg viewBox="0 0 16 16" fill="none" stroke="currentColor" stroke-width="1.2">
          <circle cx="8" cy="8" r="7.2"/>
          <rect x="5.5" y="3.8" width="5" height="8.4" rx="1"/>
          <line x1="7.3" y1="10.8" x2="8.7" y2="10.8"/>
        </svg>
        555 014 2387
      </li>
      <li>
        <svg viewBox="0 0 16 16" fill="none" stroke="currentColor" stroke-width="1.2">
          <circle cx="8" cy="8" r="7.2"/>
          <rect x="4" y="5.2" width="8" height="5.6"/>
          <polyline points="4,5.2 8,8.6 12,5.2"/>
        </svg>
        info@lodgebridgely.net
      </li>
      <li>
        <svg viewBox="0 0 16 16" fill="none" stroke="currentColor" stroke-width="1.2">
          <circle cx="8" cy="8" r="7.2"/>
          <circle cx="8" cy="8" r="4.2"/>
          <ellipse cx="8" cy="8" rx="1.8" ry="4.2"/>
          <line x1="3.8" y1="8" x2="12.2" y2="8"/>
        </svg>
        www.lodgebridgely.net
      </li>
    </ul>
  </section>

</body>
</html>
```